Mental Health Therapy Website

I need a design for a mental health therapy website. It is a private practice. The business name is Brindle Counseling, PLLC. My name is Martin Hale, LMHC, NCC, DCC. I would like some of the features/menus to be Home; Welcome/About Me, Rates and Services, Common Questions, and Contact.
If possible I would like a blog on the main page that I can update with articles I write. I would like the contact page to feature a map to my location (4318 Cedarbend Ave. E, Lakewood, WA 98499).
I would like to place a small photo of me on the Welcome/About page.
I am new to this so if I am forgetting anything, please ask me!!
I will upload my logo so you can fit it and the color scheme into the design.
Thank you so very much!

```html
<!DOCTYPE html>
<html lang="en">
<head>
<meta charset="utf-8">
<title>Brindle Counseling, PLLC – About Me</title>
<link rel="stylesheet" href="https://fonts.googleapis.com/css2?family=Open+Sans:wght@300;400;600;700&display=swap">
<style>
  :root {
    --brand-blue: #2b98d0;
    --heading-blue: #2a8fc8;
    --logo-blue: #2f5f8f;
    --band-blue: #8fbccf;
    --text-dark: #444444;
    --text-body: #666666;
    --text-muted: #8a8a8a;
    --rule: #d6d6d6;
    --rule-light: #e6e6e6;
    --card-border: #e3e3e3;
    --white: #ffffff;
    --photo-light: #e8eef3;
    --photo-mid: #b9c7d3;
    --photo-dark: #7e8d99;
  }
  * { box-sizing: border-box; margin: 0; padding: 0; }
  html, body {
    width: 1200px; height: 723px; overflow: hidden;
    background: var(--white);
    font-family: "Open Sans", Arial, sans-serif;
    color: var(--text-body);
  }
  .page { position: relative; width: 1200px; height: 723px; }

  .color-strip {
    position: absolute; top: 0; left: 0; width: 100%; height: 4px;
    background: linear-gradient(90deg,
      #e4007c 0 6%, #f39200 6% 12%, #95c11f 12% 18%, #00a0e3 18% 24%,
      #e4007c 24% 30%, #ffcc00 30% 36%, #009640 36% 42%, #35b6e9 42% 48%,
      #c2185b 48% 54%, #f39200 54% 60%, #95c11f 60% 66%, #00a0e3 66% 72%,
      #e4007c 72% 78%, #ffcc00 78% 84%, #009640 84% 90%, #35b6e9 90% 95%, #f39200 95% 100%);
  }

  .site-header { position: absolute; top: 4px; left: 0; width: 100%; height: 73px; }
  .brand {
    position: absolute; left: 96px; top: 12px;
    display: flex; align-items: center; gap: 8px;
  }
  .brand-mark { width: 34px; height: 34px; border-radius: 50%; background: var(--logo-blue); }
  .brand-name {
    font-size: 24px; font-weight: 600; color: var(--logo-blue); line-height: 1.05;
  }
  .main-nav { position: absolute; top: 19px; left: 538px; display: flex; }
  .main-nav a {
    display: block; height: 35px; line-height: 35px; padding: 0 19px;
    font-size: 12px; color: var(--text-dark); text-decoration: none;
    text-transform: uppercase; border-radius: 3px;
  }
  .main-nav a.is-active { background: var(--brand-blue); color: var(--white); }
  .header-band {
    position: absolute; top: 75px; left: 0; width: 100%; height: 10px;
    border-top: 2px solid var(--band-blue);
    background: linear-gradient(var(--white) 0 2px, var(--band-blue) 2px 100%);
  }

  .section-title {
    position: absolute; top: 119px; left: 37px;
    font-size: 30px; font-weight: 300; color: var(--heading-blue);
    letter-spacing: 0.3px;
  }
  .section-title strong { font-weight: 700; }
  .title-rule {
    position: absolute; top: 163px; left: 37px; width: 1139px; height: 5px;
    border-top: 1px solid var(--rule-light); border-bottom: 1px solid var(--rule-light);
  }

  .profile-card {
    position: absolute; top: 201px; left: 37px; width: 236px; height: 322px;
    border: 1px solid var(--card-border); border-radius: 4px; overflow: hidden;
  }
  .profile-photo {
    width: 100%; height: 270px;
    background: linear-gradient(135deg, var(--photo-light) 0%, var(--photo-mid) 55%, var(--photo-dark) 100%);
  }
  .social-links { display: flex; justify-content: center; gap: 7px; margin-top: 11px; }
  .social-links span {
    width: 30px; height: 30px; border: 1px solid var(--card-border); border-radius: 3px;
  }

  .profile-details { position: absolute; top: 200px; left: 294px; width: 688px; }
  .profile-name { font-size: 23px; font-weight: 700; color: var(--heading-blue); text-transform: uppercase; }
  .profile-role { font-size: 10px; color: var(--text-muted); text-transform: uppercase; margin-top: -2px; }
  .detail-list { margin-top: 15px; }
  .detail-row {
    display: flex; border-bottom: 1px solid var(--rule);
    padding: 13px 0 14px; font-size: 12px; line-height: 17.5px;
  }
  .detail-row dt { width: 109px; flex: none; font-weight: 600; color: var(--text-dark); }
  .detail-row dd { color: var(--text-body); }
  .appointment-button {
    display: inline-block; margin-top: 10px; width: 176px; height: 38px; line-height: 38px;
    text-align: center; background: var(--brand-blue); color: var(--white);
    font-size: 13px; border-radius: 4px; text-decoration: none;
  }
</style>
</head>
<body>
<div class="page">
  <div class="color-strip"></div>
  <header class="site-header">
    <div class="brand">
      <span class="brand-mark"></span>
      <span class="brand-name">Brindle Counseling</span>
    </div>
    <nav class="main-nav">
      <a href="#">Home</a>
      <a href="#" class="is-active">About Me</a>
      <a href="#">Rates and Services</a>
      <a href="#">Common Questions</a>
      <a href="#">Contact</a>
    </nav>
  </header>
  <div class="header-band"></div>

  <h1 class="section-title">MEET <strong>SPECIALIST</strong></h1>
  <div class="title-rule"></div>

  <aside class="profile-card">
    <div class="profile-photo" role="img" aria-label="Portrait photo of the therapist in a white coat using a tablet"></div>
    <div class="social-links" aria-label="Social links">
      <span></span><span></span><span></span>
    </div>
  </aside>

  <section class="profile-details">
    <h2 class="profile-name">Mr. Martin Hale</h2>
    <p class="profile-role">Trauma Certified Therapist</p>
    <dl class="detail-list">
      <div class="detail-row"><dt>Speciality</dt><dd>Physiotherapist</dd></div>
      <div class="detail-row"><dt>Degrees</dt><dd>LMHC, NCC, DCC</dd></div>
      <div class="detail-row"><dt>Experience</dt><dd>18 years of Experience</dd></div>
      <div class="detail-row"><dt>About him</dt><dd>Lorem ipsum dolor sit amet, consectetur adipiscing elit. Donec nec eros eget nisl fringilla commodo. Lorem ipsum dolor sit amet, consectetur adipiscing elit. Donec nec eros eget nisl fringilla commodo. Lorem ipsum dolor sit amet, consectetur adipiscing elit. Donec nec eros eget nisl fringilla commodo. Lorem ipsum dolor sit amet, consectetur adipiscing elit. Donec nec eros eget nisl fringilla commodo ornare, augue.</dd></div>
      <div class="detail-row"><dt>Work days</dt><dd>Monday - Friday</dd></div>
    </dl>
    <a href="#" class="appointment-button">Make an Appointment</a>
  </section>
</div>
</body>
</html>
```